FAST TURN AROUND - Yoga & Sound Meditation Event Flyer

Our organization - Tarrow Guidance Alliance - is currently looking for someone to create a flyer for an upcoming Yoga & Sound Meditation Event.

We are looking for the following deliverables:
Versions of the Flyer created for Social Media (Long Story & Square Post) that includes the following information. (Not including the categories)
Event Title: Tarrow Flow & Hum Unwind Session - Bayline Mix
Event Date & Time: Wednesday, April 20 | 7P - 9P
Event Location: Reedhall at Cobbleyard
Tarrow Logo: (Both black and white versions are attached. Feel free to use whichever makes more sense based on the lighting)

We would want a version of this for the eight different background images provided. For the test, you can submit 1-2 since the rest of the details will be the same once we chose the information design.

```html
<!DOCTYPE html>
<html lang="en">
<head>
<meta charset="utf-8">
<title>Tarrow Flow &amp; Hum Unwind Session – Flyer</title>
<link rel="stylesheet" href="https://fonts.googleapis.com/css2?family=Sorts+Mill+Goudy&family=Montserrat:wght@400;600&display=swap">
<style>
  :root {
    --paper: #eafcdc;
    --leaf: #84d454;
    --leaf-soft: #acd98c;
    --leaf-deep: #4d961c;
    --ink: #231f20;
    --photo-dark: #3a3132;
    --photo-mid: #8a7a72;
  }
  * { margin: 0; padding: 0; box-sizing: border-box; }
  html, body { width: 979px; height: 1200px; overflow: hidden; background: var(--paper); }
  .flyer {
    position: relative;
    width: 979px;
    height: 1200px;
    background: var(--paper);
    overflow: hidden;
    color: var(--ink);
  }
  .foliage {
    position: absolute;
    background: linear-gradient(160deg, var(--leaf-soft), var(--leaf));
    opacity: .55;
  }
  .foliage--top-left { left: 0; top: 0; width: 300px; height: 130px; border-radius: 0 0 100% 0; opacity: .35; }
  .foliage--top-right { right: 0; top: 0; width: 280px; height: 170px; border-radius: 0 0 0 100%; opacity: .35; }
  .foliage--bottom-left { left: 0; bottom: 20px; width: 250px; height: 250px; border-radius: 0 100% 0 0; opacity: .7; }
  .foliage--bottom-right { right: 0; bottom: 120px; width: 125px; height: 210px; border-radius: 100% 0 0 0; opacity: .7; }
  .rings { position: absolute; right: 0; top: 97px; width: 146px; height: 226px; }
  .brand {
    position: absolute;
    top: 78px;
    left: 0;
    width: 100%;
    text-align: center;
    font-family: "Montserrat", sans-serif;
    font-weight: 600;
    font-size: 36px;
    letter-spacing: -0.5px;
    color: var(--ink);
  }
  .brand__dot {
    display: inline-block;
    width: 14px; height: 14px;
    border-radius: 50%;
    background: var(--ink);
    margin-left: 6px;
    vertical-align: baseline;
  }
  .lotus {
    position: absolute;
    left: 209px; top: 190px;
    width: 620px; height: 540px;
    border-radius: 50%;
    background: radial-gradient(circle, var(--leaf) 55%, rgba(132,212,84,0) 72%);
  }
  .portrait {
    position: absolute;
    left: 310px; top: 255px;
    width: 418px; height: 420px;
    border-radius: 46% 46% 40% 40%;
    background: radial-gradient(ellipse at 50% 30%, var(--photo-mid) 0%, var(--photo-dark) 60%);
  }
  .details {
    position: absolute;
    left: 0; width: 100%;
    top: 760px;
    text-align: center;
  }
  .details__title {
    font-family: "Sorts Mill Goudy", serif;
    font-weight: 400;
    font-size: 32px;
    line-height: 40px;
    -webkit-text-stroke: 0.6px var(--ink);
  }
  .details__label {
    font-family: "Sorts Mill Goudy", serif;
    font-size: 24px;
    margin-top: 26px;
  }
  .details__value {
    font-family: "Montserrat", sans-serif;
    font-size: 25px;
    margin-top: 6px;
  }
  .details__label--location { margin-top: 30px; }
  .ground { position: absolute; left: 0; bottom: 0; width: 979px; height: 150px; }
</style>
</head>
<body>
<main class="flyer">
  <div class="foliage foliage--top-left" role="img" aria-label="Fine-line palm fronds in soft green"></div>
  <div class="foliage foliage--top-right" role="img" aria-label="Fine-line palm fronds in soft green"></div>

  <svg class="rings" viewBox="0 0 146 226" aria-hidden="true">
    <circle cx="146" cy="113" r="113" fill="var(--leaf-soft)"/>
    <circle cx="146" cy="113" r="75" fill="var(--paper)"/>
    <circle cx="146" cy="113" r="56" fill="var(--leaf-soft)"/>
    <circle cx="146" cy="113" r="34" fill="var(--paper)"/>
  </svg>

  <header class="brand">Tarrow Guidance Alliance<span class="brand__dot"></span></header>

  <div class="lotus" role="img" aria-label="Green lotus flower frame"></div>
  <div class="portrait" role="img" aria-label="Photo of a participant meditating with hands pressed together"></div>

  <section class="details">
    <h1 class="details__title">Tarrow Flow &amp; Hum Unwind Session<br>Bayline Mix</h1>
    <p class="details__label">Date &amp; Time</p>
    <p class="details__value">Wednesday, April 20 | 7PM - 9PM</p>
    <p class="details__label details__label--location">Location</p>
    <p class="details__value">Reedhall at Cobbleyard</p>
  </section>

  <svg class="ground" viewBox="0 0 979 150" preserveAspectRatio="none" aria-hidden="true">
    <path d="M0 100 C90 108 200 90 300 60 C340 45 360 0 430 10 C520 25 580 60 660 35 C740 5 820 15 979 60 L979 150 L0 150 Z" fill="var(--leaf-deep)"/>
  </svg>

  <div class="foliage foliage--bottom-left" role="img" aria-label="Illustrated green leaves"></div>
  <div class="foliage foliage--bottom-right" role="img" aria-label="Illustrated green leafy branch"></div>
</main>
</body>
</html>
```